Banner
Zielgruppe
Wir sind Estrichleger und Beschichter. Wir erstellen u. a. Sichtestrich und Beschichtungen im Wohnbereich und für Gewerbekunden im Industriebereich (Hallen und Tiefgaragen).
Unsere Zielgruppe sind sowohl Privatverbraucher im gehobenen Segment als auch Bauträger und Gewerbekunden
Aufgabenstellung
Gute Lesbarkeit, klare Botschaft auch wenn die Banner in großer Höhe angebracht werden.
Masse:
Bauzaunbanner aus Mesh-Plane, 340x173 cm,
wird gedruckt auf
hochwertige Mehs-Plane, rundum, umsäumt und veröst, 4/0-farbig (einseitig mit Motiv bedruck), 270 g Meshgewebe-Plane - winddurchlässig und wetterfest, (B1- zertifiziert - schwer entflammbar nach DIN 4102)
Es ist wünschenswert den Claim: 'Ich steh drauf' mit auf dem Banner zu platzieren.
Wir haben gerade die Fahrzeuge neu designen lassen, der Gewinner ist hochgeladen. Gern können Sie sich an diesem orientieren.

```html
<!DOCTYPE html>
<html lang="de">
<head>
<meta charset="utf-8">
<title>Estrichleger &amp; Beschichter – Bauzaunbanner</title>
<link rel="stylesheet" href="https://fonts.googleapis.com/css2?family=Roboto+Condensed:wght@700&family=Roboto:wght@400;500&display=swap">
<style>
  :root {
    --orange: #e8643a;
    --slate: #545860;
    --text-grey: #4a4f57;
    --white: #ffffff;
    --screed-light: #e4e1dc;
    --screed-mid: #d2cfca;
    --screed-dark: #b9b7b3;
  }
  html, body {
    margin: 0;
    padding: 0;
    width: 1200px;
    height: 848px;
    overflow: hidden;
    background: var(--white);
  }
  .banner {
    position: relative;
    width: 1200px;
    height: 848px;
    overflow: hidden;
    font-family: "Roboto", Arial, sans-serif;
  }
  .banner__photo {
    position: absolute;
    left: 0;
    top: 0;
    width: 1200px;
    height: 748px;
    background:
      radial-gradient(ellipse at 75% 45%, var(--screed-light) 0%, rgba(228,225,220,0) 55%),
      linear-gradient(160deg, var(--screed-light) 0%, var(--screed-mid) 60%, var(--screed-dark) 100%);
  }
  .logo-box {
    position: absolute;
    left: 75px;
    top: 70px;
    width: 276px;
    height: 180px;
    background: var(--orange);
    display: flex;
    align-items: center;
    justify-content: center;
  }
  .logo-box__name {
    font-family: "Roboto Condensed", "Arial Narrow", sans-serif;
    font-weight: 700;
    font-size: 85px;
    color: var(--white);
    line-height: 1;
  }
  .headline {
    position: absolute;
    left: 72px;
    top: 336px;
    margin: 0;
    font-family: "Roboto Condensed", "Arial Narrow", sans-serif;
    font-weight: 700;
    font-size: 104px;
    line-height: 103px;
    letter-spacing: -1.5px;
    color: var(--orange);
    text-transform: uppercase;
    white-space: nowrap;
  }
  .subline {
    position: absolute;
    left: 74px;
    top: 548px;
    margin: 0;
    font-weight: 500;
    font-size: 48px;
    line-height: 57px;
    color: var(--text-grey);
    white-space: nowrap;
  }
  .contact-bar {
    position: absolute;
    left: 0;
    top: 748px;
    width: 1200px;
    height: 100px;
    background: var(--slate);
    color: var(--white);
    font-size: 52px;
    line-height: 52px;
    font-weight: 400;
  }
  .contact-bar__web {
    position: absolute;
    left: 66px;
    top: 25px;
  }
  .contact-bar__phone {
    position: absolute;
    right: 61px;
    top: 25px;
  }
</style>
</head>
<body>
  <div class="banner">
    <div class="banner__photo" role="img" aria-label="Handwerker verteilt mit orangem Handschuh und Zahnkelle flüssigen grauen Estrich auf dem Boden"></div>

    <div class="logo-box">
      <span class="logo-box__name">LOGO</span>
    </div>

    <h1 class="headline">Ihr Estrichleger<br>&amp; Beschichter</h1>

    <p class="subline">Sichtestrich &amp; Beschichtungen<br>für Privat &amp; Gewerbe</p>

    <div class="contact-bar">
      <span class="contact-bar__web">www.estrich-beispiel.de</span>
      <span class="contact-bar__phone">Tel. 09876 - 54 32 1</span>
    </div>
  </div>
</body>
</html>
```